Web Page Design for a Website that Provides Tutoring

I am looking to create an online tutoring website. The website will allow parents or students to contact tutors with a view to instructing them to tutor themselves or their children.

The name of the website is LendYourLessons.

This brief is to create the design for one of the web pages for this web site. I am hoping the same designer will be available to design other pages.

The page I want designed is one of the more complex and I have attached the design as an excel spreadsheet. The web page needs to include all the items on this page but if you want to change the positioning of the items then Im fine with that.

I recently had two logos created for this website. My favourite is the one with a mortar board but im not sure I like the colours. I have attached both of these logos and you can use either of them, change the colours or create something different. I just want a design pleasing to the eye. If the logo is changed I would like that in a seperate file.

So can you please submit designs for this page. I have attached the two logos which you can use, change or if you feel you have a better idea then you can use that.

On the spreadsheet the Send Message, Favourite etc are buttons.

Target Market(s)

People who want to better themselves.
Possible middle class to upper class.

Industry/Entity Type

Tutoring

Number of Pages Required

1 page

Requirements
Must have
• The designs must have alot of the information attached in the spreadsheet.

```html
<!DOCTYPE html>
<html lang="en">
<head>
<meta charset="utf-8">
<title>LendYourLessons – Tutor Profile</title>
<link href="https://fonts.googleapis.com/css2?family=Open+Sans:wght@400;600;700&family=Bebas+Neue&family=Londrina+Solid:wght@400&display=swap" rel="stylesheet">
<style>
:root{
  --navy:#22233a;
  --navy-deep:#24233d;
  --orange:#f07d1a;
  --yellow:#f0b400;
  --teal:#2ea784;
  --teal-dark:#1f8a63;
  --teal-light:#3db89a;
  --purple:#565a8f;
  --purple-dark:#2f3160;
  --red:#e0161c;
  --peach:#f5b98a;
  --green:#7dc242;
  --text:#444;
  --muted:#777;
  --line:#e2e2e2;
  --footer:#22222a;
  --footer-text:#8a8a96;
}
*{box-sizing:border-box;margin:0;padding:0}
html,body{width:1200px;height:2436px;overflow:hidden}
body{position:relative;font-family:"Open Sans",Arial,sans-serif;color:var(--text);background:#fff;font-size:13px}
svg{display:block}

/* header */
.site-header{position:absolute;left:0;top:0;width:1200px;height:73px;background:var(--navy)}
.brand{position:absolute;left:73px;top:20px;display:flex;align-items:center;gap:8px;color:var(--orange);font-weight:700;font-size:26px;letter-spacing:-.5px}
.brand-mark{width:14px;height:14px;background:var(--orange);border-radius:50%}
.main-nav a{position:absolute;top:28px;color:#fff;text-decoration:none;font-size:13px}
.main-nav a.current::after{content:"";position:absolute;left:0;right:0;top:22px;height:3px;background:var(--orange)}
.account{position:absolute;left:994px;top:28px;color:#fff;font-size:13px;display:flex;align-items:center;gap:6px}

/* hero */
.hero{position:absolute;left:0;top:73px;width:1200px;height:481px;background:#f3f6f6}
.hero-photo{position:absolute;left:0;top:0;width:660px;height:481px;background:linear-gradient(100deg,#d9dedf 0%,#eef1f1 35%,#3b4a66 55%,#dfe4e4 75%,#f3f6f6 100%)}
.hi-bubble{position:absolute;left:600px;top:94px;width:82px;height:82px;border-radius:50%;background:var(--orange);color:#fff;font-family:Georgia,serif;font-size:38px;display:flex;align-items:center;justify-content:center}
.hi-bubble::after{content:"";position:absolute;left:12px;bottom:-12px;border-left:14px solid transparent;border-right:5px solid transparent;border-top:20px solid var(--orange);transform:rotate(20deg)}
.hero-title{position:absolute;left:720px;top:106px;font-family:"Londrina Solid",sans-serif;font-weight:400;font-size:50px;color:var(--teal-light);line-height:1;white-space:nowrap}
.hero-sub{position:absolute;left:721px;top:168px;font-size:32px;color:#555;font-weight:400;line-height:40px}
.hero-text{position:absolute;left:721px;top:241px;width:420px;font-size:13px;line-height:20px;color:#555}
.btn{position:absolute;display:flex;align-items:center;justify-content:center;gap:8px;color:#fff;font-weight:700;font-size:12px;text-transform:uppercase;border-radius:3px}
.btn-orange{background:var(--orange)}
.btn-teal{background:var(--teal)}

/* panels */
.panel{position:absolute;top:554px;width:400px;height:310px;color:#fff}
.panel-contact{left:0;background:var(--yellow)}
.panel-schedule{left:400px;background:var(--teal)}
.panel-reviews{left:800px;background:var(--purple)}
.panel-title{position:absolute;top:26px;font-family:"Bebas Neue",sans-serif;font-weight:400;font-size:34px;letter-spacing:.5px}
.field{position:absolute;left:73px;width:255px;background:#fff;border-radius:2px;color:#555;font-size:12px;padding:8px 10px}
.schedule-lead{position:absolute;left:73px;top:32px;width:250px;font-weight:700;font-size:14px;line-height:20px}
.checks{position:absolute;left:73px;top:92px;list-style:none}
.checks li{display:flex;align-items:center;gap:9px;height:31.5px;font-size:12.5px}
.rating-line{position:absolute;left:69px;top:78px;display:flex;align-items:center;gap:6px;font-size:11px}
.stars{color:var(--yellow);font-size:16px;letter-spacing:1px}
.bar-row{position:absolute;left:69px;display:flex;align-items:center;font-size:10px;height:14px}
.bar-row span.lbl{width:39px}
.bar{width:92px;height:8px;background:#fff}
.bar.full{background:var(--yellow)}
.bar-row span.pct{margin-left:7px}
.share{position:absolute;left:69px;top:206px;font-size:12.5px}

/* stats */
.stats{position:absolute;top:922px;font-size:12.5px;color:#555}
.stats .row{position:relative;height:37px;border-bottom:1px solid var(--line)}
.stats .row:last-child{border-bottom:none}
.stats .row span{position:absolute;top:8px}
.stats .head span{font-weight:700;color:#333}
.divider{position:absolute;left:602px;top:918px;width:1px;height:146px;background:var(--line)}
.feedback{position:absolute;left:361px;top:5px;width:139px;height:22px;background:var(--red);color:#fff;border-radius:2px;font-size:12px;font-weight:700;display:flex;align-items:center;justify-content:center;gap:6px}

/* subjects */
.subjects{position:absolute;left:73px;top:1112px;width:1052px;border-collapse:collapse;font-size:12.5px}
.subjects th{background:#8a8a8a;color:#fff;height:36px;text-align:left;font-weight:700}
.subjects td{background:#ececec;height:37px;border-top:2px solid #fff;color:#555}

/* availability */
.section-title{position:absolute;font-weight:700;font-size:19px;color:#333}
.underline{position:absolute;height:3px;width:33px;background:var(--orange)}
.calendar{position:absolute;left:73px;top:1358px;width:627px;height:414px;border:4px solid #e6e6e6;background:#fff}
.cal-month{position:absolute;left:39px;top:24px;font-size:17px;font-weight:600;color:#333}
.cal-cell{position:absolute;width:26px;height:26px;margin-left:-13px;margin-top:-13px;border-radius:50%;display:flex;align-items:center;justify-content:center;font-size:13px;color:#888}
.cal-cell.dow{font-size:12px;color:#555;width:40px;margin-left:-20px;border-radius:0}
.cal-cell.muted{color:#aaa}
.cal-cell.avail{background:var(--green);color:#fff}
.cal-cell.taken{background:var(--red);color:#fff}
.cal-cell.reserved{background:var(--peach);color:#fff}
.cal-line{position:absolute;left:20px;width:540px;height:1px;background:#eee}
.tooltip{position:absolute;left:98px;top:220px;border:1px solid #ccc;background:#fff;font-size:10px;color:#666;padding:1px 6px;display:flex;align-items:center;gap:4px}
.legend{position:absolute;left:705px;top:1358px;width:419px;height:414px;background:var(--navy-deep)}
.legend-item{position:absolute;left:63px;width:244px;height:37px;border-bottom:1px solid #3a3956;display:flex;align-items:center;gap:10px;color:#fff;font-size:12.5px}
.legend-item:last-child{border-bottom:none}
.swatch{width:14px;height:14px}

/* reviews */
.review{position:absolute;top:1895px;width:340px}
.review h3{font-size:15px;font-weight:700;color:#333}
.review .date{font-size:11px;color:#555;margin-top:4px}
.review p{font-size:12.5px;line-height:20px;color:#555;margin-top:17px}
.review .rate{display:flex;align-items:center;gap:8px;font-size:10.5px;color:#555;margin-top:20px}

/* footer */
.site-footer{position:absolute;left:0;top:2092px;width:1200px;height:344px;background:var(--footer);color:var(--footer-text);font-size:12.5px}
.foot-col{position:absolute;top:40px}
.foot-col h4{color:#fff;font-size:13px;font-weight:700;margin-bottom:16px}
.foot-col p,.foot-col li{line-height:20px}
.foot-col ul{list-style:none}
.foot-col li{line-height:26px}
.foot-input{width:242px;border-bottom:1px solid #555;height:28px;padding-top:8px;margin-top:6px}
.foot-submit{margin-top:14px;width:242px;height:33px;background:var(--teal);color:#fff;font-weight:700;font-size:12px;display:flex;align-items:center;justify-content:center}
.socials{display:flex;gap:8px;margin-top:34px}
.socials span{width:34px;height:34px;border-radius:50%}
.copyright{position:absolute;left:435px;top:295px;font-size:12px}
</style>
</head>
<body>

<header class="site-header">
  <div class="brand"><span class="brand-mark"></span>LendYourLessons</div>
  <nav class="main-nav">
    <a class="current" style="left:404px">Home</a>
    <a style="left:472px">Search</a>
    <a style="left:543px">Student</a>
    <a style="left:620px">Tutor</a>
    <a style="left:684px">About</a>
    <a style="left:750px">Contact</a>
  </nav>
  <div class="account">
    <svg width="13" height="13" viewBox="0 0 14 14"><circle cx="7" cy="4" r="3.2" fill="#f07d1a"/><path d="M1 14c0-4 3-6 6-6s6 2 6 6z" fill="#f07d1a"/></svg>
    Login &nbsp;or&nbsp; Register
  </div>
</header>

<section class="hero">
  <div class="hero-photo" role="img" aria-label="Photo of a smiling tutor in a suit pointing at a whiteboard"></div>
  <div class="hi-bubble">Hi.</div>
  <h1 class="hero-title">My name is Clara</h1>
  <div class="hero-sub">I am....</div>
  <p class="hero-text">Industry's standard dummy text ever since the 1500s, when an unknown printer took a galley of type and scrambled it to make a type specimen book. It essentially unchanged.</p>
  <div class="btn btn-orange" style="left:721px;top:338px;width:153px;height:32px">
    <svg width="13" height="13" viewBox="0 0 14 14"><path d="M2 12l1-4 7-7 3 3-7 7z" fill="#fff"/></svg>Register Today</div>
  <div class="btn btn-teal" style="left:885px;top:338px;width:164px;height:32px">
    <svg width="15" height="11" viewBox="0 0 16 11"><rect x="0" y="1" width="11" height="9" rx="1" fill="#fff"/><path d="M11 5l5-4v9z" fill="#fff"/></svg>Watch Our Demo</div>
</section>

<section class="panel panel-contact">
  <h2 class="panel-title" style="left:73px">Contact Tutor</h2>
  <div class="field" style="top:81px;height:36px">Name</div>
  <div class="field" style="top:122px;height:35px">Email</div>
  <div class="field" style="top:164px;height:65px">Message</div>
  <div class="btn btn-orange" style="left:73px;top:239px;width:255px;height:47px;font-size:14px">
    <svg width="18" height="13" viewBox="0 0 18 13"><rect x="3" y="0" width="15" height="13" fill="#fff"/><path d="M3 0l7.5 7L18 0" stroke="#f07d1a" stroke-width="1.5" fill="none"/><rect x="0" y="4" width="2" height="1.5" fill="#fff"/><rect x="0" y="8" width="2" height="1.5" fill="#fff"/></svg>Send Message</div>
</section>

<section class="panel panel-schedule">
  <p class="schedule-lead">She Would like to know your schedule.</p>
  <ul class="checks">
    <li><svg width="14" height="14" viewBox="0 0 14 14"><circle cx="7" cy="7" r="6" stroke="#fff" stroke-width="1.5" fill="none"/><path d="M4 7l2 2 4-4" stroke="#fff" stroke-width="1.5" fill="none"/></svg>Offline Lessons</li>
    <li><svg width="14" height="14" viewBox="0 0 14 14"><circle cx="7" cy="7" r="6" stroke="#fff" stroke-width="1.5" fill="none"/><path d="M4 7l2 2 4-4" stroke="#fff" stroke-width="1.5" fill="none"/></svg>Affordable Rates</li>
    <li><svg width="14" height="14" viewBox="0 0 14 14"><circle cx="7" cy="7" r="6" stroke="#fff" stroke-width="1.5" fill="none"/><path d="M4 7l2 2 4-4" stroke="#fff" stroke-width="1.5" fill="none"/></svg>1-on-1 Tutoring</li>
    <li><svg width="14" height="14" viewBox="0 0 14 14"><circle cx="7" cy="7" r="6" stroke="#fff" stroke-width="1.5" fill="none"/><path d="M4 7l2 2 4-4" stroke="#fff" stroke-width="1.5" fill="none"/></svg>Refund Policy</li>
  </ul>
  <div class="btn" style="left:68px;top:239px;width:255px;height:47px;background:var(--teal-dark);font-size:14px">
    <svg width="14" height="15" viewBox="0 0 14 15"><circle cx="7" cy="4" r="3.5" fill="#fff"/><path d="M0 15c0-5 3-6.5 7-6.5s7 1.5 7 6.5z" fill="#fff"/></svg>Contact Favor</div>
</section>

<section class="panel panel-reviews">
  <h2 class="panel-title" style="left:69px">Customer Reviews</h2>
  <div class="rating-line"><span class="stars">★★★★★</span>15 (5.0 out of 5 stars)</div>
  <div class="bar-row" style="top:106px"><span class="lbl">5 Star</span><span class="bar full"></span><span class="pct">100%</span></div>
  <div class="bar-row" style="top:125px"><span class="lbl">4 Star</span><span class="bar"></span><span class="pct">0%</span></div>
  <div class="bar-row" style="top:144px"><span class="lbl">3 Star</span><span class="bar"></span><span class="pct">0%</span></div>
  <div class="bar-row" style="top:163px"><span class="lbl">2 Star</span><span class="bar"></span><span class="pct">0%</span></div>
  <div class="bar-row" style="top:180px"><span class="lbl">1 Star</span><span class="bar"></span><span class="pct">0%</span></div>
  <p class="share">Share your thoughts with other customers</p>
  <div class="btn" style="left:70px;top:239px;width:257px;height:47px;background:var(--purple-dark);font-size:14px">
    <svg width="14" height="14" viewBox="0 0 14 14"><path d="M1 13l1-4 7-7 3 3-7 7z" fill="#fff"/></svg>Write A Review</div>
</section>

<section class="stats" style="left:73px;width:500px">
  <div class="row"><span style="left:0">Review Score</span><span style="left:180px">4.5/5</span><span style="left:359px">Member Since</span></div>
  <div class="row"><span style="left:0">Reliability</span><span style="left:180px">4.0/5.0</span><span style="left:359px">Last Logged In</span></div>
  <div class="row"><span style="left:0">Punctuality</span><span style="left:180px">4.6/5</span>
    <div class="feedback"><svg width="11" height="11" viewBox="0 0 12 12"><path d="M0 6l12-6-4 12-2-5z" fill="#fff"/></svg>Leave Feedback</div></div>
</section>
<div class="divider"></div>
<section class="stats" style="left:627px;width:498px">
  <div class="row head"><span style="left:0">Tutoring Type</span><span style="left:182px">In Personal Only</span><span style="left:360px">Teacher</span></div>
  <div class="row"><span style="left:0">Willing To Travel</span><span style="left:182px">Home Only</span><span style="left:360px">Full Time Tutor</span></div>
  <div class="row"><span style="left:0">Age</span><span style="left:182px">20</span><span style="left:360px">Full Time Student</span></div>
  <div class="row"><span style="left:0">DBS (CRB)</span></div>
</section>

<table class="subjects">
  <colgroup><col style="width:208px"><col style="width:140px"><col style="width:154px"><col style="width:123px"><col style="width:142px"><col style="width:151px"><col></colgroup>
  <tr><th style="padding-left:27px">Subject Taught</th><th>Primary</th><th>Secondary</th><th>GCSE</th><th>A-LEVEL</th><th>University</th><th>Adult Learner</th></tr>
  <tr><td style="padding-left:27px">Biology</td><td>£20</td><td></td><td>£25</td><td>£30</td><td></td><td></td></tr>
  <tr><td style="padding-left:27px">Chemistry</td><td>£20</td><td></td><td>£25</td><td>£30</td><td></td><td></td></tr>
</table>

<h2 class="section-title" style="left:73px;top:1278px">Availability</h2>
<div class="underline" style="left:73px;top:1316px"></div>

<div class="calendar">
  <div class="cal-month">November 2016 &nbsp;›</div>
  <div class="cal-line" style="top:76px"></div>
  <div class="cal-line" style="top:128px"></div>
  <div class="cal-line" style="top:186px"></div>
  <div class="cal-line" style="top:243px"></div>
  <div class="cal-line" style="top:300px"></div>
  <div class="cal-line" style="top:358px"></div>
  <div class="cal-cell dow" style="left:50px;top:90px">SUN</div>
  <div class="cal-cell dow" style="left:132px;top:90px">MON</div>
  <div class="cal-cell dow" style="left:215px;top:90px">TUE</div>
  <div class="cal-cell dow" style="left:298px;top:90px">WED</div>
  <div class="cal-cell dow" style="left:381px;top:90px">THU</div>
  <div class="cal-cell dow" style="left:464px;top:90px">FRI</div>
  <div class="cal-cell dow" style="left:547px;top:90px">SAT</div>
  <div class="cal-cell muted" style="left:50px;top:147px">30</div>
  <div class="cal-cell muted" style="left:132px;top:147px">31</div>
  <div class="cal-cell muted" style="left:215px;top:147px">1</div>
  <div class="cal-cell muted" style="left:298px;top:147px">2</div>
  <div class="cal-cell muted" style="left:381px;top:147px">3</div>
  <div class="cal-cell muted" style="left:464px;top:147px">4</div>
  <div class="cal-cell reserved" style="left:547px;top:147px">5</div>
  <div class="cal-cell muted" style="left:50px;top:205px">6</div>
  <div class="cal-cell avail" style="left:132px;top:205px">7</div>
  <div class="cal-cell avail" style="left:215px;top:205px">8</div>
  <div class="cal-cell muted" style="left:298px;top:205px">9</div>
  <div class="cal-cell taken" style="left:381px;top:205px">10</div>
  <div class="cal-cell muted" style="left:464px;top:205px">11</div>
  <div class="cal-cell muted" style="left:547px;top:205px">12</div>
  <div class="tooltip"><svg width="9" height="9" viewBox="0 0 10 10"><circle cx="5" cy="5" r="4.2" stroke="#888" fill="none"/><path d="M5 2.5v2.5h2" stroke="#888" fill="none"/></svg>12:39pm</div>
  <div class="cal-cell muted" style="left:50px;top:262px">13</div>
  <div class="cal-cell muted" style="left:132px;top:262px">14</div>
  <div class="cal-cell muted" style="left:215px;top:262px">15</div>
  <div class="cal-cell muted" style="left:298px;top:262px">16</div>
  <div class="cal-cell muted" style="left:381px;top:262px">17</div>
  <div class="cal-cell taken" style="left:464px;top:262px">18</div>
  <div class="cal-cell muted" style="left:547px;top:262px">19</div>
  <div class="cal-cell muted" style="left:50px;top:319px">20</div>
  <div class="cal-cell muted" style="left:132px;top:319px">21</div>
  <div class="cal-cell reserved" style="left:215px;top:319px">22</div>
  <div class="cal-cell muted" style="left:298px;top:319px">23</div>
  <div class="cal-cell muted" style="left:381px;top:319px">24</div>
  <div class="cal-cell muted" style="left:464px;top:319px">25</div>
  <div class="cal-cell muted" style="left:547px;top:319px">26</div>
  <div class="cal-cell muted" style="left:50px;top:382px">27</div>
  <div class="cal-cell muted" style="left:132px;top:382px">28</div>
  <div class="cal-cell muted" style="left:215px;top:382px">29</div>
  <div class="cal-cell muted" style="left:298px;top:382px">30</div>
  <div class="cal-cell muted" style="left:381px;top:382px">1</div>
  <div class="cal-cell muted" style="left:464px;top:382px">2</div>
  <div class="cal-cell muted" style="left:547px;top:382px">3</div>
</div>

<aside class="legend">
  <div class="legend-item" style="top:52px"><span class="swatch" style="background:var(--green)"></span>Available</div>
  <div class="legend-item" style="top:89px"><span class="swatch" style="background:var(--red)"></span>Taken</div>
  <div class="legend-item" style="top:125px"><span class="swatch" style="background:var(--peach)"></span>Reserved</div>
  <div class="legend-item" style="top:162px"><span class="swatch" style="background:#7a3fb0"></span>No</div>
</aside>

<h2 class="section-title" style="left:0;width:1200px;text-align:center;top:1821px">Tutors Reviews</h2>
<div class="underline" style="left:584px;top:1860px"></div>

<article class="review" style="left:76px">
  <h3>Owen Hartley</h3><div class="date">12 Dec 2016 | 12:39pm</div>
  <p>" Reference site about Lorem Ipsum, giving information on its origins, as well as a random Lipsum generator."</p>
  <div class="rate"><span class="stars">★★★★½</span>(Star Rateing 4.5)</div>
</article>
<article class="review" style="left:435px">
  <h3>Owen Hartley</h3><div class="date">12 Dec 2016 | 12:39pm</div>
  <p>" Reference site about Lorem Ipsum, giving information on its origins, as well as a random Lipsum generator."</p>
  <div class="rate"><span class="stars">★★★★½</span>(Star Rateing 4.5)</div>
</article>
<article class="review" style="left:796px">
  <h3>Owen Hartley</h3><div class="date">12 Dec 2016 | 12:39pm</div>
  <p>" Reference site about Lorem Ipsum, giving information on its origins, as well as a random Lipsum generator."</p>
  <div class="rate"><span class="stars">★★★★½</span>(Star Rateing 4.5)</div>
</article>

<footer class="site-footer">
  <div class="foot-col" style="left:73px">
    <h4>Get Our Newsletter</h4>
    <p style="width:250px">To receive updates about my tutor, Join our newsletter.</p>
    <div class="foot-input">Name</div>
    <div class="foot-input">Email</div>
    <div class="foot-submit">SUBMIT</div>
  </div>
  <div class="foot-col" style="left:435px">
    <h4>Contact Us</h4>
    <p>228 Lorem Ipsum dolor,<br>Dosis amet, -85485</p>
    <p style="margin-top:22px">T: 1800 555 010<br>E: info@lendyourlessons.com</p>
    <div class="socials"><span style="background:#3b5998"></span><span style="background:#3fb3e6"></span><span style="background:#dd4b39"></span></div>
  </div>
  <div class="foot-col" style="left:705px">
    <h4>Quick Links</h4>
    <ul><li>Home</li><li>Search</li><li>Student</li><li>Tutor</li><li>About</li><li>Contact</li></ul>
  </div>
  <div class="foot-col" style="left:885px">
    <h4>Info Links</h4>
    <ul><li>Register as a Student</li><li>Register as a Paretnt</li><li>Register as a Tutor</li></ul>
  </div>
  <div class="copyright">Copyright 2016 Lend Your Lessons. All Rights Reserved.</div>
</footer>

</body>
</html>
```